Coral Ridge Distillery Company Ltd needs new Rum Brand label/logo

We need a logo/label design for a brand new distillery opening in Jamaica WI.
The company will be initially producing alcohol spirit beverage and we are due to launch a new product to the industry that research shows has never been attempted before. The first sample batch will be ready in mid January 2014 and the initial samples will be in 200 ml nocturne bottles with screw cap and cork. bottles will be clear and some will be translucent in claret colour. Transparent label would be good on clear bottles as liquid contained will be red in colour. The product name will be CANE GLOW so this needs to be the main focal point of the label other than the company name. Other details are: 42% Alc/Vol 200 ml Jamaica Rum prepared and bottled by Coral Ridge Distillery Co Ltd.

Target Market(s)

Target market for this product will be buyers and distributors internationally.

Font styles to use
Decorative
Script

Requirements
Must have
• Label must have the family crest situated on the label perhaps in a corner or in middle of label but not to out perform the focal point being the product name ( CANE GLOW )

```html
<!DOCTYPE html>
<html lang="en">
<head>
<meta charset="utf-8">
<title>Cane Glow – Jamaica Rum Label</title>
<link rel="stylesheet" href="https://fonts.googleapis.com/css2?family=Rye&family=Alfa+Slab+One&family=Oswald:wght@500&family=Mrs+Saint+Delafield&family=Josefin+Sans:wght@600&display=swap">
<style>
  :root {
    --paper: #ffffff;
    --maroon: #4f1a1a;
    --maroon-deep: #3a1010;
    --ink: #231515;
    --gold: #c2923f;
    --gold-dark: #7c5a22;
    --flag-green: #1f9a3a;
    --flag-gold: #f6cf1d;
    --flag-black: #111111;
  }
  * { margin: 0; padding: 0; box-sizing: border-box; }
  html, body { width: 1200px; height: 902px; overflow: hidden; background: var(--paper); }
  .canvas { position: relative; width: 1200px; height: 902px; background: var(--paper); }
  .label-art { position: absolute; inset: 0; }
  .ribbon-text {
    font-family: "Josefin Sans", sans-serif;
    font-weight: 600;
    font-size: 26px;
    letter-spacing: 6px;
    fill: var(--ink);
  }
  .brand-name {
    position: absolute; left: 0; right: 0; top: 300px;
    text-align: center;
    font-family: "Rye", serif;
    font-size: 104px;
    line-height: 1;
    color: var(--maroon);
    letter-spacing: 2px;
  }
  .strength {
    position: absolute; left: 0; right: 0; top: 432px;
    text-align: center;
    font-family: "Josefin Sans", sans-serif;
    font-weight: 600;
    font-size: 28px;
    color: var(--ink);
    letter-spacing: 1px;
  }
  .style-name {
    position: absolute; left: 0; right: 0; top: 491px;
    text-align: center;
    font-family: "Alfa Slab One", serif;
    font-size: 32px;
    color: var(--paper);
    letter-spacing: 2px;
  }
  .producer {
    position: absolute; left: 0; right: 0; top: 570px;
    text-align: center;
    font-family: "Mrs Saint Delafield", cursive;
    font-size: 40px;
    line-height: 34px;
    color: var(--ink);
  }
  .volume {
    position: absolute; left: 0; right: 0; top: 690px;
    text-align: center;
    font-family: "Oswald", sans-serif;
    font-weight: 500;
    font-size: 28px;
    color: var(--ink);
  }
</style>
</head>
<body>
<main class="canvas">
  <svg class="label-art" width="1200" height="902" viewBox="0 0 1200 902">
    <defs>
      <linearGradient id="crest-tone" x1="0" y1="0" x2="0" y2="1">
        <stop offset="0" stop-color="#d9ad5a"/>
        <stop offset="1" stop-color="#9c7230"/>
      </linearGradient>
      <path id="estd-path" d="M418,248 Q480,192 548,196"/>
      <path id="year-path" d="M652,196 Q720,192 782,248"/>
    </defs>

    <!-- left date ribbon -->
    <g class="ribbon" fill="none" stroke="var(--ink)" stroke-width="2">
      <path d="M400,232 Q468,168 548,174"/>
      <path d="M420,266 Q482,208 548,214"/>
      <path d="M400,232 q-16,14 -2,30 q12,10 22,4"/>
      <path d="M800,232 Q732,168 652,174"/>
      <path d="M780,266 Q718,208 652,214"/>
      <path d="M800,232 q16,14 2,30 q-12,10 -22,4"/>
    </g>
    <text class="ribbon-text"><textPath href="#estd-path" startOffset="50%" text-anchor="middle">ESTD</textPath></text>
    <text class="ribbon-text"><textPath href="#year-path" startOffset="50%" text-anchor="middle">2014</textPath></text>

    <!-- family crest area -->
    <path class="crest" role="img" aria-label="Family crest with helm, mantling and shield"
          d="M562,138 H638 V238 Q638,282 600,292 Q562,282 562,238 Z"
          fill="url(#crest-tone)" stroke="var(--gold-dark)" stroke-width="2"/>

    <!-- strength rules -->
    <g stroke="var(--maroon)" stroke-width="3">
      <line x1="420" y1="449" x2="525" y2="449"/>
      <line x1="675" y1="449" x2="780" y2="449"/>
    </g>

    <!-- style banner -->
    <g class="style-banner">
      <line x1="330" y1="512" x2="870" y2="512" stroke="var(--ink)" stroke-width="2"/>
      <path d="M330,512 l8,-6 l8,6 l-8,6 z M870,512 l-8,-6 l-8,6 l8,6 z" fill="var(--ink)"/>
      <path d="M382,484 H818 q12,0 12,10 V536 q-8,-12 -20,-8 H390 q-12,-4 -20,8 V494 q0,-10 12,-10 z"
            fill="var(--maroon-deep)"/>
      <rect x="392" y="490" width="416" height="40" fill="none" stroke="var(--paper)" stroke-width="1.5"/>
    </g>

    <!-- Jamaican flag -->
    <g class="flag" transform="translate(560 748)">
      <rect width="80" height="44" fill="var(--flag-green)"/>
      <path d="M0,0 L40,22 L0,44 Z M80,0 L40,22 L80,44 Z" fill="var(--flag-black)"/>
      <path d="M0,0 L80,44 M80,0 L0,44" stroke="var(--flag-gold)" stroke-width="7"/>
    </g>
  </svg>

  <h1 class="brand-name">CANE GLOW</h1>
  <p class="strength">42% ALC</p>
  <p class="style-name">JAMAICA RUM</p>
  <p class="producer">Prepared And Bottled By<br>Coral Ridge<br>Distillery Co Ltd.</p>
  <p class="volume">VOL 200 ML</p>
</main>
</body>
</html>
```